Newsletter Design Project

We are looking at refreshing our corporate newsletter and general communication design.
The design will be a corporate design for our brand:
VRIL - Northern Journey Planners Guild
For brand colours, requirements and logo look here: www.vrilguild-example.org/media
or check the attached documents.

We need to incorporate logo and brand but we are happy to refresh the palette.

Important! Attached please also find designs and colour palette of our new website-newsletter should complement these.

You are also free to use photos from events some of which can be found here:
http://www.examplebook.test/pages/Northern-Journey-Planners-Guild/904517263380419?sk=photos_stream

We attached a sample of our newsletter. We usually include sections such as:
-CONTENTS (for navigation)
-INTRODUCTION
-NEW MEMBERS
-EVENTS
-FEATURES
-IN THE MEDIA
-ABOUT VRIL

Most important:
-PROFESSIONAL AUDIENCE-PROFESSIONAL DESIGN
-SIMPLE (see example our homepage in attachment)
-IMAGES AND GRAPHS OK
-DESIGN TO BE RE-USABLE FOR OTHER COMMUNICATIONS
-HTML format please
Updates

We are happy to increase the budget if the design is right

We have uploaded new social media icons which we would like integrated in  the design

I have uploaded a new high res version of the map that you can integrate in your designs (feel free to change colour scheme if needed)

I have also posted another Chirpnet + corporate social media icon (as some mentioned it wasn't working)

Target Market(s)

B2B- audience includes various tourism companies

Industry/Entity Type

Communication

```html
<!DOCTYPE html>
<html lang="en">
<head>
<meta charset="utf-8">
<title>VRIL Newsletter</title>
<link href="https://fonts.googleapis.com/css2?family=Questrial&family=Cinzel:wght@500;700&display=swap" rel="stylesheet">
<style>
:root{
  --navy:#13204a;
  --navy-deep:#0d1838;
  --body-blue:#2b3d7a;
  --strip-blue:#4f7ac4;
  --header-sky:#c9d9ee;
  --ribbon:#2a93c9;
  --ribbon-light:#dfe6ee;
  --lavender:#d9dcef;
  --yellow:#f6dd47;
  --white:#ffffff;
  --ink:#1a1f3a;
}
*{margin:0;padding:0;box-sizing:border-box}
html,body{width:927px;height:1200px;overflow:hidden;background:var(--white)}
.canvas{position:relative;width:927px;height:1200px;overflow:hidden;font-family:"Questrial",sans-serif;background:var(--body-blue)}
.side-strip{position:absolute;left:0;top:0;width:28px;height:1153px;background:linear-gradient(180deg,#7fa3d8,var(--strip-blue))}
.sidebar{position:absolute;left:24px;top:0;width:249px;height:1153px;background:linear-gradient(180deg,#1b2a5c,var(--navy-deep))}
.brand{position:absolute;left:90px;top:36px;width:130px;height:100px;display:flex;align-items:center;justify-content:center;gap:10px;color:var(--white);font-size:30px;letter-spacing:1px}
.brand .dot{width:12px;height:12px;border-radius:50%;background:var(--yellow)}
.ribbon{position:absolute;left:16px;width:248px;height:44px;display:flex;align-items:center;padding-left:14px;font-family:"Cinzel",serif;font-weight:700;font-size:22px;color:var(--white);background:var(--ribbon);clip-path:polygon(0 0,94% 0,100% 50%,94% 100%,0 100%)}
.ribbon.light{background:var(--ribbon-light);color:var(--navy);font-size:21px}
.ribbon.mid{background:#3a6f96;font-size:21px}
.issue-list{position:absolute;left:44px;top:270px;list-style:none;color:var(--white);font-family:"Cinzel",serif;font-size:12.5px;line-height:18.5px;font-weight:500}
.issue-list li::before{content:"- "}
.member{position:absolute;left:62px;width:170px;display:flex;align-items:center;justify-content:center;gap:8px;color:var(--white);font-size:22px}
.member .mark{width:14px;height:14px;background:var(--ribbon)}
.media-badge{position:absolute;left:40px;top:840px;width:218px;height:93px;background:var(--white);display:flex;flex-direction:column;align-items:center;justify-content:center;color:var(--navy)}
.media-badge .big{font-size:38px;line-height:1}
.media-badge .small{font-size:13px;margin-top:4px}
.tab{position:absolute;left:16px;width:68px;height:46px;background:var(--ribbon);color:var(--white);clip-path:polygon(0 0,78% 0,100% 50%,78% 100%,0 100%);padding:4px 0 0 12px;line-height:1}
.tab .n{font-size:20px;display:block}
.tab .m{font-size:11px}
.header{position:absolute;left:273px;top:0;width:654px;height:133px;background:var(--header-sky)}
.header h1{position:absolute;left:28px;top:66px;font-weight:400;font-size:23px;letter-spacing:1px;color:var(--navy);text-transform:uppercase}
.hero{position:absolute;left:273px;top:133px;width:654px;height:307px;background:linear-gradient(135deg,#3c4f78,#1f2a44 55%,#6b7da6)}
.body-bg{position:absolute;left:273px;top:440px;width:654px;height:713px;background:radial-gradient(ellipse at 60% 60%,#3b4f93,var(--body-blue) 70%)}
.intro{position:absolute;left:276px;top:444px;width:644px;height:174px;background:var(--lavender);border-radius:10px;border:1px solid #aeb4d4}
.intro p{position:absolute;left:13px;top:12px;width:326px;font-size:14.5px;line-height:19.7px;color:var(--ink)}
.intro a{color:var(--ink);font-weight:700;text-decoration:underline}
.intro-photo{position:absolute;border:3px solid var(--white);box-shadow:0 1px 4px rgba(0,0,0,.4)}
.intro-photo.one{left:348px;top:14px;width:158px;height:108px;background:linear-gradient(135deg,#6a3a2a,#3a2a28)}
.intro-photo.two{left:371px;top:48px;width:139px;height:120px;background:linear-gradient(160deg,#c9c4bb,#8c7f78)}
.article{position:absolute;left:284px;width:636px;color:var(--white);font-size:16.6px;line-height:27.3px;text-align:justify}
.footer{position:absolute;left:0;top:1153px;width:927px;height:47px;background:var(--yellow)}
.social{position:absolute;right:26px;top:5px;display:flex;gap:4px}
.social span{width:40px;height:38px;background:var(--navy-deep);border:1px solid #7f8ab0;color:var(--white);font-size:8px;display:flex;align-items:center;justify-content:center}
</style>
</head>
<body>
<div class="canvas">
  <div class="side-strip"></div>
  <aside class="sidebar"></aside>
  <div class="brand"><span class="dot"></span>VRIL</div>

  <div class="ribbon" style="top:216px">In This Issue</div>
  <ul class="issue-list">
    <li>Introduction</li><li>New Members</li><li>Events</li><li>Features</li><li>In The Media</li><li>About VRIL</li>
  </ul>

  <div class="ribbon mid" style="top:387px">New Members</div>
  <div class="member" style="top:488px"><span class="mark"></span>Brackenfield</div>
  <div class="member" style="top:657px"><span class="mark"></span>Veltora</div>

  <div class="ribbon light" style="top:769px">In The Media</div>
  <div class="media-badge"><span class="big">LPM13</span><span class="small">Lodging Partners Marketplace</span></div>

  <div class="tab" style="top:1031px"><span class="n">Top</span><span class="m">dec</span></div>
  <div class="tab" style="top:1097px;background:#3a6f96"><span class="n">15</span><span class="m">dec</span></div>

  <header class="header"><h1>Northern Journey Planners Guild</h1></header>
  <div class="hero" role="img" aria-label="Event photo: delegates meeting at tables in a conference hall"></div>
  <div class="body-bg" role="img" aria-label="Faint dotted world map background"></div>

  <section class="intro">
    <p>VRIL starts 2013 with an extensive calendar of events, campaigns and partnerships, for even more members than ever.<br>Are you signed up to the wide-ranging business opportunities?<br>If not, <a>find out more from Marisol today.</a><br><a>Like VRIL on Examplebook</a></p>
    <div class="intro-photo one" role="img" aria-label="Photo of a speaker at a lectern"></div>
    <div class="intro-photo two" role="img" aria-label="Photo of a seminar room full of attendees"></div>
  </section>

  <p class="article" style="top:651px">VRIL’s first seminar of the year takes place on the 31st January in London and focuses on educational travel. The sector is important in markets worldwide and not only shapes the travellers of the future but is also known for its innovation and ideas. We are delighted to have Tomas Reyland, a youth travel expert and CEO of Learnvoyage, to share his latest findings and insights. Further educational travel initiatives will follow in 2013, most notably during this year’s NTX in March. Kindly hosted by The Halden Archive Rooms.</p>

  <p class="article" style="top:914px">Early February sees this year’s Lodging Partners Marketplace return to Brussels for the third time. Following VRIL’s tried and tested appointment model, this highly targeted event brings contractors and hoteliers together for a full day of meetings. Sunday night sees a dinner reception at the Lakehouse Verent restaurant in Brussels, kindly hosted by event partners Orvale Visitor Board.</p>

  <footer class="footer">
    <div class="social"><span>Linkrow</span><span>Exbook</span><span>Chirpnet</span><span>Viewtube</span></div>
  </footer>
</div>
</body>
</html>
```